New DermaLoom logo and packaging

We would like a new design for our new product DermaLoom, a high strength vitamin C serum which treats pigmentation. The packaging will reflect a high quality, clinical product with the logo "DermaLoom" on the front, with it's ingredients "Vitamin C, B3, B5, E and ferulic acid" the products are in two sizes 10ml and 30ml.

This is one of many products to come out in the DermaLoom range.

It would be for high end medical clinics selling premium brands, with a strong medical and clinical feel, professional and current or even futuristic in appearance.

Gold, blue, silver, White, cream are all colours that do this (without appearing cheap)

The product is not tested on animals, so would have
- "Not tested on animals".
- "12m" symbol for shelf life,
- "Made in USA"
- and ingredients list

See attached the product and existing box

Target Market(s)

Medical and aesthetic clinics

Font styles to use
Serif
Sans Serif

Colors
33a6d7
cee9f5
ffffff
fbed22
fee18a

Requirements
Must have
• High end premium brand
Nice to have
• like the idea of gold and silver lettering on cream background
Should not have
• Tacky, over complicated design

```html
<!DOCTYPE html>
<html lang="en">
<head>
<meta charset="utf-8">
<title>DermaLoom Serum Packaging</title>
<link href="https://fonts.googleapis.com/css2?family=Questrial&display=swap" rel="stylesheet">
<style>
  :root {
    --backdrop: #e6f0ed;
    --gold: #c4952a;
    --gold-deep: #b3841f;
    --ink: #4a4a4a;
    --ink-soft: #5c5c5c;
    --marble-light: #ffffff;
    --marble-mid: #eeeeee;
    --marble-vein: #d6d6d6;
  }
  * { margin: 0; padding: 0; box-sizing: border-box; }
  html, body { width: 1200px; height: 1200px; overflow: hidden; }
  body {
    background: var(--backdrop);
    font-family: "Questrial", "Century Gothic", sans-serif;
    position: relative;
  }
  .marble {
    position: absolute;
    inset: 0;
    background:
      radial-gradient(ellipse at 30% 25%, var(--marble-light) 0%, transparent 55%),
      radial-gradient(ellipse at 75% 70%, var(--marble-light) 0%, transparent 50%),
      linear-gradient(135deg, var(--marble-mid) 0%, var(--marble-light) 35%, var(--marble-vein) 55%, var(--marble-light) 75%, var(--marble-mid) 100%);
  }
  .centered { position: absolute; left: 0; right: 0; text-align: center; }

  /* Carton front */
  .carton {
    position: absolute;
    left: 428px; top: 242px;
    width: 352px; height: 692px;
    border: 6px solid var(--gold);
    overflow: hidden;
  }
  .carton .brand { top: 128px; font-size: 48px; color: var(--gold); letter-spacing: 0.5px; }
  .carton .product { top: 302px; font-size: 33px; color: var(--gold); letter-spacing: 3px; }
  .carton .ingredients { top: 376px; font-size: 12.5px; line-height: 19px; color: var(--ink-soft); letter-spacing: 1.2px; }
  .carton .volume { top: 522px; font-size: 12px; color: var(--ink-soft); letter-spacing: 0.5px; }

  /* Bottle labels */
  .label {
    position: absolute;
    width: 204px; height: 248px;
    border-top: 5px solid var(--gold);
    border-bottom: 5px solid var(--gold);
    overflow: hidden;
  }
  .label-front { left: 164px; top: 602px; }
  .label-back { left: 843px; top: 616px; }

  .label-front .brand { top: 44px; font-size: 29px; color: var(--gold); }
  .label-front .product { top: 108px; font-size: 18px; color: var(--gold); letter-spacing: 0.5px; }
  .label-front .ingredients { top: 141px; font-size: 5.5px; color: var(--ink); letter-spacing: 0.2px; }
  .label-front .volume { top: 190px; font-size: 5.5px; color: var(--ink); }

  .label-back .brand { top: 36px; font-size: 28px; color: var(--gold); }
  .label-back .ingredients { top: 84px; font-size: 6px; line-height: 8px; color: var(--ink); }
  .label-back .claim { top: 123px; font-size: 6px; color: var(--ink); }
  .label-back .symbols {
    position: absolute; top: 149px; left: 0; right: 0;
    display: flex; justify-content: center; gap: 14px; align-items: center;
  }
  .label-back .origin { top: 199px; font-size: 6px; color: var(--ink); }
</style>
</head>
<body>

  <section class="carton">
    <div class="marble" role="img" aria-label="White and grey marble surface"></div>
    <div class="centered brand">DermaLoom</div>
    <div class="centered product">SERUM</div>
    <div class="centered ingredients">VITAMIN C, B3, B5, E<br>AND FERULIC ACID</div>
    <div class="centered volume">30 ml</div>
  </section>

  <section class="label label-front">
    <div class="marble" role="img" aria-label="White and grey marble surface"></div>
    <div class="centered brand">DermaLoom</div>
    <div class="centered product">SERUM</div>
    <div class="centered ingredients">VITAMIN C, B3, B5, E AND FERULIC ACID</div>
    <div class="centered volume">30 ml</div>
  </section>

  <section class="label label-back">
    <div class="marble" role="img" aria-label="White and grey marble surface"></div>
    <div class="centered brand">DermaLoom</div>
    <div class="centered ingredients">Ingredients: Vitamin C, B3, B5, E<br>and Ferulic Acid</div>
    <div class="centered claim">Not tested on animals</div>
    <div class="symbols">
      <svg class="recycle-badge" width="22" height="22" viewBox="0 0 22 22" aria-label="Recycling badge">
        <circle cx="11" cy="11" r="10" fill="#2b2b2b"/>
      </svg>
      <svg class="shelf-life" width="26" height="24" viewBox="0 0 26 24" aria-label="12 month shelf life">
        <path d="M4 9 L22 9 L21 21 L5 21 Z" fill="none" stroke="#2b2b2b" stroke-width="1.4"/>
        <path d="M5 7 L20 2" fill="none" stroke="#2b2b2b" stroke-width="1.4"/>
        <text x="13" y="18" font-size="6" text-anchor="middle" fill="#2b2b2b" font-family="Questrial, sans-serif">12M</text>
      </svg>
    </div>
    <div class="centered origin">Made in USA</div>
  </section>

</body>
</html>
```